BrivoLane Ute.

I want the full logo on one side. And the other side the card if right Ralf the logo the left half orange like the car in the logo color with Danielle R Morrow
Founder and CEO
Email symbol then dmorrow@brivolaneute.com
Www symbol. Then Brivolaneute.com
Phone symbol then 413-926-BRIV
The very bottom would like Brivo Lane Ute is a division of Harmond Vistas. LLC

```html
<!DOCTYPE html>
<html lang="en">
<head>
<meta charset="utf-8">
<title>Brivo Lane Ute – Business Card</title>
<link rel="stylesheet" href="https://fonts.googleapis.com/css2?family=Roboto:wght@400;500;700&display=swap">
<style>
  :root {
    --bg: #a9a9a9;
    --orange: #e98f24;
    --orange-deep: #c8741a;
    --ink: #1f1f1f;
    --muted: #5a5a5a;
    --paper: #ffffff;
    --white-text: #fff7ec;
  }
  * { margin: 0; padding: 0; box-sizing: border-box; }
  html, body { width: 1200px; height: 930px; overflow: hidden; }
  body {
    background: var(--bg);
    font-family: "Roboto", Arial, sans-serif;
    position: relative;
  }
  .card {
    position: absolute;
    width: 560px;
    height: 320px;
    box-shadow: 0 6px 14px rgba(0,0,0,0.25);
  }
  .card--front {
    left: 80px; top: 110px;
    background: var(--orange);
    display: flex; flex-direction: column; align-items: center; justify-content: center;
  }
  .card--back {
    left: 560px; top: 500px;
    background: var(--paper);
  }
  .logo-art {
    border-radius: 6px;
  }
  .card--front .logo-art {
    width: 220px; height: 78px;
    background: linear-gradient(180deg, #f3b466, var(--orange-deep));
  }
  .brand-name {
    font-family: "Roboto", Arial, sans-serif;
    font-weight: 700;
    color: var(--ink);
    letter-spacing: 1px;
    white-space: nowrap;
  }
  .card--front .brand-name { font-size: 38px; margin-top: 12px; }
  .front-web {
    margin-top: 34px;
    color: var(--white-text);
    font-size: 15px;
    letter-spacing: 0.3px;
  }
  .back-logo {
    position: absolute;
    left: 0; top: 0;
    width: 262px; height: 290px;
    display: flex; flex-direction: column; align-items: center; justify-content: center;
  }
  .back-logo .logo-art {
    width: 160px; height: 58px;
    background: linear-gradient(180deg, #f6c98d, var(--orange));
  }
  .back-logo .brand-name { font-size: 25px; margin-top: 10px; }
  .divider {
    position: absolute;
    left: 268px; top: 76px;
    width: 2px; height: 140px;
    background: var(--orange);
  }
  .contact {
    position: absolute;
    left: 292px; top: 72px;
    color: var(--ink);
    font-size: 14px;
    line-height: 1.35;
  }
  .contact__name {
    color: var(--orange);
    font-size: 19px;
    font-weight: 500;
    letter-spacing: 0.3px;
    text-transform: uppercase;
  }
  .contact__title { margin-bottom: 10px; }
  .contact__address { margin-bottom: 4px; }
  .contact__line { display: flex; align-items: center; gap: 8px; }
  .contact__line svg { width: 11px; height: 11px; flex: none; }
  .accent { color: var(--orange); }
  .division-note {
    position: absolute;
    left: 0; right: 0; bottom: 16px;
    text-align: center;
    font-size: 11px;
    color: var(--muted);
    letter-spacing: 0.3px;
  }
</style>
</head>
<body>
  <section class="card card--front" aria-label="Card front">
    <div class="logo-art" role="img" aria-label="Illustration of an orange vintage wagon with a surfboard on the roof"></div>
    <div class="brand-name">BRIVO LANE UTE</div>
    <div class="front-web">www.Brivolaneute.com</div>
  </section>

  <section class="card card--back" aria-label="Card back">
    <div class="back-logo">
      <div class="logo-art" role="img" aria-label="Illustration of an orange vintage wagon with a surfboard on the roof"></div>
      <div class="brand-name">BRIVO LANE UTE</div>
    </div>
    <div class="divider"></div>
    <div class="contact">
      <div class="contact__name">Danielle R Morrow</div>
      <div class="contact__title">Founder and CEO</div>
      <div class="contact__address">142b Kerrow Street,<br>Ashvale, NZ, 7042</div>
      <div class="contact__line">
        <svg viewBox="0 0 12 12" aria-hidden="true"><path d="M2.5 1h2l1 3-1.3 1a6 6 0 0 0 2.8 2.8l1-1.3 3 1v2a1 1 0 0 1-1 1A9.5 9.5 0 0 1 1.5 2a1 1 0 0 1 1-1z" fill="var(--orange)"/></svg>
        <span>413-926-BRIV</span>
      </div>
      <div class="contact__line">
        <svg viewBox="0 0 12 12" aria-hidden="true"><rect x="1" y="2.5" width="10" height="7" fill="none" stroke="var(--orange)" stroke-width="1.3"/><path d="M1 2.5l5 4 5-4" fill="none" stroke="var(--orange)" stroke-width="1.3"/></svg>
        <span>dmorrow@brivolaneute.com</span>
      </div>
      <div class="contact__line">
        <svg viewBox="0 0 12 12" aria-hidden="true"><circle cx="6" cy="6" r="4.8" fill="none" stroke="var(--orange)" stroke-width="1.2"/><ellipse cx="6" cy="6" rx="2" ry="4.8" fill="none" stroke="var(--orange)" stroke-width="1"/><path d="M1.2 6h9.6" stroke="var(--orange)" stroke-width="1"/></svg>
        <span>www.<span class="accent">Brivolaneute</span>.com</span>
      </div>
    </div>
    <div class="division-note">Brivo Lane Ute is a division of Harmond Vistas. LLC</div>
  </section>
</body>
</html>
```